Sam Greenfield Billboard

**Task Description: Billboard Design for Self Storage Facility**

**Objective:**
Design a captivating billboard to promote our self-storage facility with a focus on our convenient location and online rental capabilities.

**Key Messages to Include:**
1. **Location Emphasis:** Highlight that our facility is located right beside the billboard (maybe by using an arrow pointing left).
2. **Online Rental Convenience:** Feature prominently that customers can "Rent Online Anytime!” or that we are "Always Open Online!"

**Target Audience:**
- Local residents looking for convenient self-storage solutions.
- Businesses needing storage space accessible around the clock.

**Design Elements:**
1. **Visual Impact:** Eye-catching graphics and colors that stand out against the surroundings.
2. **Clear Text:** Bold and concise messaging that can be read and understood quickly.
3. **Contact Information:** Include our phone number and website URL for easy access to further information.

**Additional Information:**
- Billboard dimensions: 12 ft. x 24 ft.
- Preferred color scheme: Bright and attention-grabbing, but professional.
- Branding: Incorporate our logo and brand colors to maintain consistency.

**Deliverables:**
- High-resolution digital file compatible with billboard printing specifications.
- Consider mockups or visualizations for presentation purposes.

Please note that I have attached current logos/graphics that we would love to incorporate into the billboard as well as a picture of our current billboard. Our logo (Sam Greenfield Self Storage - SG navy.png) MUST be incorporated into the billboard. Also feel free to add any of the current descriptions from the picture of our current billboard into the design. Instead of using "Climate Controlled" use "Temperature Controlled". Thank you for your attention to these details. We look forward to reviewing your proposed design!

```html
<!DOCTYPE html>
<html lang="en">
<head>
<meta charset="UTF-8">
<title>Sam Greenfield Billboard</title>
<link href="https://fonts.googleapis.com/css2?family=Montserrat:wght@700;800&display=swap" rel="stylesheet">
<style>
  :root {
    --navy: #0b2259;
    --bronze: #93714f;
    --sky: #00aeef;
    --white: #ffffff;
    --stage: #585858;
    --steel-light: #d9d9d9;
    --steel-mid: #b9b9b9;
  }
  html, body {
    margin: 0;
    width: 1200px;
    height: 1200px;
    overflow: hidden;
    background: var(--stage);
  }
  .billboard {
    position: absolute;
    left: 30px;
    top: 315px;
    width: 1840px;
    height: 920px;
    transform: scale(0.6196);
    transform-origin: 0 0;
    overflow: hidden;
    background: var(--steel-light);
  }
  .billboard svg {
    position: absolute;
    left: 0;
    display: block;
  }
  .billboard text {
    font-family: "Montserrat", sans-serif;
    font-weight: 700;
  }
  .facility-photo {
    position: absolute;
    inset: 0 0 auto 0;
    height: 642px;
    background: radial-gradient(ellipse at 50% 60%, #ececec 0%, var(--steel-light) 40%, var(--steel-mid) 100%);
  }
  .brand-lockup { top: 0; }
  .brand-lockup text { fill: var(--navy); }
  .tagline-band { top: 516px; }
  .tagline-band text { fill: var(--white); }
  .info-panel { top: 642px; }
  .info-panel text { fill: var(--white); }
  .info-panel .phone-number { font-weight: 800; }
</style>
</head>
<body>
  <main class="billboard">
    <div class="facility-photo" role="img" aria-label="Greyscale photo of a self storage corridor lined with roll-up unit doors"></div>

    <svg class="brand-lockup" width="1840" height="500" viewBox="0 0 1840 500" aria-label="Sam Greenfield Self Storage">
      <rect x="168" y="96" width="1502" height="246" fill="none" stroke="var(--bronze)" stroke-width="8"/>
      <text x="209" y="302" font-size="178" textLength="1425" lengthAdjust="spacingAndGlyphs">SAM GREENFIELD</text>
      <text x="372" y="452" font-size="92" textLength="1100" lengthAdjust="spacing">SELF STORAGE</text>
    </svg>

    <svg class="tagline-band" width="1840" height="106" viewBox="0 0 1840 106">
      <rect width="1840" height="106" fill="var(--bronze)"/>
      <text x="109" y="80" font-size="74" textLength="1620" lengthAdjust="spacingAndGlyphs">SELF STORAGE IN THE HEART OF GEORGIA</text>
    </svg>

    <svg class="info-panel" width="1840" height="278" viewBox="0 0 1840 278">
      <rect width="1840" height="278" fill="var(--navy)"/>
      <polygon points="0,37 1000,37 968,119 0,119" fill="var(--sky)"/>
      <text x="49" y="100" font-size="60" textLength="910" lengthAdjust="spacingAndGlyphs">TEMPERATURE CONTROLLED</text>
      <text x="1037" y="100" font-size="60" textLength="732" lengthAdjust="spacingAndGlyphs">RENT ONLINE ANYTIME</text>

      <g class="phone-icon" transform="translate(46,166)" aria-hidden="true">
        <path d="M10 6 L20 4 L26 20 L19 25 Q22 38 31 47 L38 42 L50 52 L46 62 Q30 66 16 48 Q4 30 10 6 Z" fill="var(--sky)"/>
        <path d="M32 14 Q42 18 44 30" fill="none" stroke="var(--sky)" stroke-width="4" stroke-linecap="round"/>
        <path d="M34 4 Q52 10 54 30" fill="none" stroke="var(--sky)" stroke-width="4" stroke-linecap="round"/>
      </g>
      <text class="phone-number" x="114" y="234" font-size="96" textLength="630" lengthAdjust="spacingAndGlyphs">555 014 2290</text>

      <polygon points="762,154 1840,154 1840,236 794,236" fill="var(--sky)"/>
      <text x="806" y="214" font-size="64" textLength="970" lengthAdjust="spacingAndGlyphs">www.samgreenfieldstorage.com</text>
    </svg>
  </main>
</body>
</html>
```